Invitation annual meeting 2017 of Corvelle Group (2017 Annual Staff Appointments)

Version française: We want to create an invitation to the annual meeting of Groupe Corvelle. This invitation will also be printed as a poster. You will find enclosed a photo of a "B" made with the employees of the Group during an internal event. You will absolutely have this photo on the invitation. I also send it to you when you save it while waiting for the invitation. The invitation must be festive, elegant and classy, ​​because it will take place on the 18th of December, just before Christmas (on the theme of Christmas and New Year Eve). Please, do not use the color "red" on this invitation. You can use this gray: Pantone 431 C for this invitation if you want to. The annual meeting of the staff (annual meeting) 18 December 2017 (18th) of December 2017) Marlindôme (at Marlindome) From 5pm to 9.30pm (from 5pm to 9.30pm) French version: On the occasion of the annual meeting of the staff we wish to make an invitation which will also be printed as a poster. You will find in the attached elements a photo of a B made on the beach with employees. It will be necessary to use this B imperatively for your creation. I am also sending you the quick save the date we had done while waiting for the invitation. This one must be classy, ​​festive because the event will take place on December 18th, with the approach of the end-of-year celebrations (thematic New Year's Eve and non-christmas). You can use anthracite gray: Pantone 431C The group logo should appear on the invitation. Text: Annual Staff Meeting 18 December 2017 Marlindôme from 5pm to 9.30pm
Updates

Project Deadline Extended Reason: Hello We give two more days on the project because we have not been fully seduced by the proposals received so far. Added Tuesday, October 24, 2017

Target Market(s)

ENG: Internal ==> employees of the Corvelle Group FR: internal to the Group

Colors

Requirements
Must have
• ENG: It is obligatory to use the photo of the "B" on the beach for this invitation. You can crop the image of the B if you want to. FR: B "made by employees" of the transmitted photo (possibility of detaching it)
Should not have
• ENG: Boat photos, "kitsch" designs and the color red EN: the pictures of boats, the "kitsch", the red

```html
<!DOCTYPE html>
<html lang="fr">
<head>
<meta charset="utf-8">
<title>Trophées – Groupe Corvelle</title>
<link rel="stylesheet" href="https://fonts.googleapis.com/css2?family=Righteous&display=swap">
<style>
  :root {
    --backdrop: #5c5e5d;
    --paper: #ffffff;
    --sand-light: #f7c47e;
    --sand-deep: #f09a55;
    --foam: #f3e7d0;
    --sea-light: #22bba0;
    --sea-deep: #0c6f8c;
    --crowd-a: #4a5fa8;
    --crowd-b: #7a5aa6;
    --anthracite: #3e4144;
    --veil: rgba(255, 255, 255, 0.55);
  }
  html, body {
    margin: 0;
    padding: 0;
    width: 1000px;
    height: 1200px;
    overflow: hidden;
    background: var(--backdrop);
  }
  .poster {
    position: absolute;
    left: 130px;
    top: 18px;
    width: 755px;
    height: 1162px;
    background: var(--paper);
  }
  .poster__art {
    position: absolute;
    left: 0;
    top: 0;
    width: 755px;
    height: 1162px;
  }
  .poster__title {
    font-family: "Righteous", sans-serif;
    fill: var(--veil);
  }
  .poster__frame {
    fill: none;
    stroke: var(--veil);
    stroke-width: 24;
  }
  .event-details {
    font-family: "Righteous", sans-serif;
    fill: var(--anthracite);
  }
  .event-details__label { font-size: 21px; }
  .event-details__date { font-size: 30px; }
  .event-details__place { font-size: 20px; }
</style>
</head>
<body>
  <main class="poster">
    <svg class="poster__art" viewBox="0 0 755 1162" width="755" height="1162">
      <defs>
        <linearGradient id="beach-gradient" x1="0" y1="0" x2="1" y2="0.15">
          <stop offset="0" stop-color="var(--sand-deep)"/>
          <stop offset="0.3" stop-color="var(--sand-light)"/>
          <stop offset="0.49" stop-color="var(--sand-light)"/>
          <stop offset="0.52" stop-color="var(--foam)"/>
          <stop offset="0.56" stop-color="var(--sea-light)"/>
          <stop offset="1" stop-color="var(--sea-deep)"/>
        </linearGradient>
        <linearGradient id="crowd-gradient" x1="0" y1="0" x2="1" y2="1">
          <stop offset="0" stop-color="var(--crowd-a)"/>
          <stop offset="1" stop-color="var(--crowd-b)"/>
        </linearGradient>
      </defs>

      <polygon class="beach-photo" role="img"
               aria-label="Aerial photo of a sandy beach meeting a turquoise sea"
               points="32,25 726,25 726,1119 32,897"
               fill="url(#beach-gradient)"/>

      <text class="poster__title" x="60" y="306" font-size="140"
            textLength="632" lengthAdjust="spacingAndGlyphs">TROPHEES</text>

      <rect class="poster__frame" x="154" y="379" width="397" height="396"/>

      <rect class="crowd-photo" role="img"
            aria-label="Aerial photo of the employees standing on the beach to form a letter B"
            x="194" y="412" width="326" height="330" rx="10"
            fill="url(#crowd-gradient)" opacity="0.9"/>

      <g class="event-details">
        <text class="event-details__label" x="32" y="1046">Rencontre annuelle du personnel</text>
        <text class="event-details__date" x="32" y="1084">18 décembre 2017</text>
        <text class="event-details__place" x="32" y="1112">Marlindôme · de 17h à 21h30</text>
      </g>
    </svg>
  </main>
</body>
</html>
```